Buchcover für rechtliche Unterstützung von Verantwortungsträgern in Druckereien zum Thema Reklamation
Super engagiert , ging auch auf Sonderwünsche ein und hat einen fantastischen Support gegeben.
Zielgruppe
Wir unterstützen deutschlandweit all diejenigen Verantwortungsträger in Druckereien die bei einer späteren Reklamation von Kunden und Liefernatenverträgen den Kopf hinhalten müssen , indem wir mit unserem System die Sinne für 90% aller im Alltag vorkommenden Vertragsfallen schärfen.
Aufgabenstellung
Titel : Rechtzeitig klug handeln
SL : Einige etwas andere Blicke auf Verträge und Versicherungen der Druckindustrie. Eine Pflichtlektüre für Verantwortliche im Vertrieb und Einkauf und QM des Etiketten- ,und Verpackungsdrucks
Zielgruppe sind Verantwortungsträger in Druckereien wie Einkauf , Vertrieb, Qualitätsmanagement , Geschäftsleitung ( Männer und Frauen gleichermaßen ) eher konservativ , technikorientiert
Vielen Dank für die tollen Vorschläge. Meine Idee war aber mich als Experten zu positionieren . Das Buichg soll auch somit einen Wiedererkennungseffekt bilden. Ich habe einbmal amn Wochenende gesammelt und mich einmal selbst am Layout versucht.

```html
<!DOCTYPE html>
<html lang="de">
<head>
<meta charset="utf-8">
<title>Rechtzeitig klug handeln – Buchumschlag</title>
<link rel="stylesheet" href="https://fonts.googleapis.com/css2?family=Roboto+Condensed:wght@400;700&family=Zilla+Slab:wght@700&display=swap">
<style>
  :root {
    --cyan: #00ffff;
    --magenta: #ff00ff;
    --yellow: #ffff00;
    --grey: #666666;
    --black: #000000;
    --white: #ffffff;
    --symbol-grey: #999999;
    --page: #ffffff;
    --sans: "Roboto Condensed", "Arial Narrow", sans-serif;
    --slab: "Zilla Slab", "Rockwell", serif;
  }
  * { margin: 0; padding: 0; box-sizing: border-box; }
  html, body { width: 1200px; height: 878px; overflow: hidden; background: var(--page); }
  .cover { position: relative; width: 1200px; height: 878px; }
  .block { position: absolute; }

  .cyan { background: var(--cyan); }
  .magenta { background: var(--magenta); }
  .yellow { background: var(--yellow); }
  .black { background: var(--black); }
  .grey { background: var(--grey); }

  .author-photo {
    position: absolute; left: 59px; top: 296.6px; width: 189.7px; height: 284.8px;
    background: linear-gradient(160deg, #b5b2ae 0%, #9c9895 45%, #3a3a3c 75%, #1e1e20 100%);
  }
  .blurb {
    position: absolute; left: 304px; top: 317px;
    font-family: var(--sans); font-size: 12px; line-height: 17.8px;
    color: var(--white); white-space: nowrap;
  }
  .blurb span { display: block; }

  .spine-text {
    position: absolute; writing-mode: vertical-rl; transform: rotate(180deg);
    color: var(--white); white-space: nowrap;
  }
  .spine-title {
    left: 581.4px; width: 37.2px; top: 296.6px; height: 284.8px;
    display: flex; align-items: center; justify-content: center;
    font-family: var(--slab); font-weight: 700; font-size: 18px;
  }
  .spine-author {
    left: 581.4px; width: 37.2px; top: 581.4px; height: 284.9px;
    display: flex; align-items: center; justify-content: center;
    font-family: var(--sans); font-weight: 700; font-size: 14px;
  }

  .title {
    position: absolute; left: 618.6px; width: 569.8px; top: 308px;
    text-align: center; color: var(--white); font-family: var(--slab); font-weight: 700;
  }
  .title-main { display: block; font-size: 76px; line-height: 82px; letter-spacing: -1px; }
  .title-sub { display: block; font-size: 46px; line-height: 50px; }

  .subtitle {
    position: absolute; left: 618.6px; width: 569.8px; top: 478px;
    text-align: center; color: var(--white);
    font-family: var(--sans); font-size: 15px; line-height: 20.5px;
  }
  .subtitle p + p { margin-top: 4px; }

  .front-author {
    position: absolute; left: 689px; top: 820px;
    font-family: var(--sans); font-weight: 700; font-size: 17.5px; color: var(--black);
  }
  .paragraph-mark {
    position: absolute; left: 903.5px; width: 284.9px; top: 581.4px; height: 284.9px;
    display: flex; align-items: center; justify-content: flex-end; padding-right: 72px;
    font-family: var(--slab); font-weight: 700; font-size: 190px; line-height: 1;
    color: var(--symbol-grey);
  }
</style>
</head>
<body>
<div class="cover">
  <!-- back cover -->
  <div class="block cyan" style="left:11.7px;top:11.7px;width:284.9px;height:284.9px"></div>
  <div class="block magenta" style="left:296.6px;top:11.7px;width:284.8px;height:284.9px"></div>
  <div class="block grey" style="left:11.7px;top:296.6px;width:569.7px;height:284.8px"></div>
  <div class="block yellow" style="left:11.7px;top:581.4px;width:284.9px;height:284.9px"></div>
  <div class="block black" style="left:296.6px;top:581.4px;width:284.8px;height:284.9px"></div>

  <div class="author-photo" role="img" aria-label="Porträtfoto des Autors vor grauer Betonwand"></div>

  <div class="blurb">
    <span>Lorem ipsum dolor sit amet, consetetur</span>
    <span>sadipscing elitr, sed diam nonumy eirmod</span>
    <span>tempor invidunt ut labore et dolore magna</span>
    <span>aliquyam erat, sed diam voluptua. At vero eos</span>
    <span>et accusam et justo duo dolores et ea rebum.</span>
    <span>Stet clita kasd gubergren, no sea takimata</span>
    <span>sanctus est Lorem ipsum dolor sit amet.</span>
    <span>Lorem ipsum dolor sit amet, consetetur</span>
    <span>sadipscing elitr, sed diam nonumy eirmod</span>
    <span>tempor invidunt ut labore et dolore magna</span>
    <span>aliquyam erat, sed diam voluptua. At vero eos</span>
    <span>et accusam et justo duo dolores et ea rebum.</span>
    <span>Stet clita kasd gubergren, no sea takimata</span>
    <span>sanctus est.</span>
  </div>

  <!-- spine -->
  <div class="block yellow" style="left:581.4px;top:11.7px;width:37.2px;height:284.9px"></div>
  <div class="block black" style="left:581.4px;top:296.6px;width:37.2px;height:284.8px"></div>
  <div class="block magenta" style="left:581.4px;top:581.4px;width:37.2px;height:284.9px"></div>
  <div class="spine-text spine-title">Rechtzeitig klug handeln</div>
  <div class="spine-text spine-author">Vorname Nachname</div>

  <!-- front cover -->
  <div class="block cyan" style="left:618.6px;top:11.7px;width:284.9px;height:284.9px"></div>
  <div class="block magenta" style="left:903.5px;top:11.7px;width:284.9px;height:284.9px"></div>
  <div class="block grey" style="left:618.6px;top:296.6px;width:569.8px;height:284.8px"></div>
  <div class="block yellow" style="left:618.6px;top:581.4px;width:284.9px;height:284.9px"></div>
  <div class="block black" style="left:903.5px;top:581.4px;width:284.9px;height:284.9px"></div>

  <h1 class="title">
    <span class="title-main">Rechtzeitig</span>
    <span class="title-sub">klug handeln</span>
  </h1>

  <div class="subtitle">
    <p>Einige etwas andere Blicke<br>auf Verträge und Versicherungen der Druckindustrie.</p>
    <p>Eine Pflichtlektüre für Verantwortliche<br>im Vertrieb, Einkauf und QM des Etiketten- und Verpackungsdrucks</p>
  </div>

  <div class="front-author">Vorname Nachname</div>
  <div class="paragraph-mark" aria-hidden="true">§</div>
</div>
</body>
</html>
```